"Voltrane" - Sci-Fi Movie Poster

I need a movie poster to help raise funds for my upcoming sci-fi film entitled "Voltrane".
UPDATE: Please no space. No spaceships. No aliens.
FOR REFERENCE - HERE'S THE STORY LOGLINE:
Set in the near future, when his ex-girlfriend's research lab is on the cusp of an Artificial Intelligence breakthrough - enabling the human mind to be immortally preserved, idealistic hacker Rob is compelled to infiltrate her company and steal the invention for a rival tycoon.
POSTER TAGLINE: "When some become immortal the rest of us are dead."
POSSIBLE IMAGERY (these are from the script set in the near future which, at first glance, looks reasonably familiar but upon really looking is surprisingly different):
1) Modestly-sized Digital Billboards (not huge like in Cinderpath) display ads to "preserve your memories" showing virtual versions of the recently deceased giving advice to their living descendants.
2) Machines build machines (huge 3D printers even directly print regular-sized 3D printers). Robots, which are now distinctly designed to not even attempt to look particularly human, replace most (but not all) people's jobs.
3) City scenes where 90% of storefronts are conspicuously closed or repurposed. One "delivery re-distribution center" for Brivo/Quellix/Tropa/Hensmark and run jointly by Lunoquo and KMR and DRTQ clearly looks like it fairly recently was a pretty big Pellingham's drive-through restaurant.
4) No street parking and almost no traffic because 95% of vehicles are driverless (the few who still drive are either wealthy or luddite/anti-technology).
5) Parking garages hold countless, stacked sleeping-'Pods' for the semi-homeless.
6) Pizza & Parcel Drones deliver directly to windows on the high floors of tall buildings.
NOTE: Don't feel compelled to include any of those possible images above. I want cool, creative and unique (more than simply doing exactly what I suggest).
CREATIVE DIRECTIVES:
Top Priority = "Provocative" and/or "Visually compelling" and/or "Ironic"
Middle Priority = "Unique" and/or "Avant-garde" and/or "Stylized"
Low Priority = Maybe consider leaving space/placeholders for 2 or 3 actors' faces to be included in the poster (as well as a "billing block" of credits at the bottom).
THANKS AND GOOD KARMA TO YOU!

Reason: There are few cool design directions but none are meeting the project's needs. It's good to come up with something unique and different so long as it fits the story. So please don't include anything that's prohibited. So that means: no aliens, no space, no spaceships, no light sabers, no magic. Please consider the story points in the creative overview description. Also please seriously consider making the poster look happy, pleasant, normal from a distance but when we look closely we see the future is different (or scary or ironic or even funny). THANKS AND GOOD KARMA TO YOU ALL! warm regards, Lew

Industry/Entity Type

Movie

Font styles to use
Sans Serif

Colors

Designer to choose colors to be used in the design.

Requirements
Must have
• Must feel like smart "hard sci-fi" - meaning it could/will really happen in the future (it's not "fantasy"). In other words, it should also not feel silly, cheesy, or crazy. PLEASE WATCH AND CONSIDER THE WISE LESSONS OF THIS CLIPNEST VIDEO entitled "Where Did Cinema Art Wander Off?": https://www.clipnest-example.net/view?c=QpLm83TzRw
Nice to have
• A cool, unique color palette (though I personally kinda like yellow & blue). Comparable films to "VOLTRANE" include: "Veloria", "Hollow Loom", "Braider", "Quarter 6", "Silent Verdict". Posters I like include some of those for: "Braider", "Quarter 6", "Undertow", "Brannoc: Emberfall", "Few Wake", "Signal Fen", "Kelp", "The Grey Drifters - season 1 poster", "Dusk". But this story has no space, no spaceships, no aliens and the future looks very, very similar to today. Thanks.
Should not have
• Not normally a big fan of "minimalist" posters but I try to be openminded. In any event, it absolutely must not have cliches or ripoffs of other movies. I hate cliches and I won't accept anything that's directly stealing from a single source. But if you want to be inspired by and combine multiple sources in a new, unique way then that's great!

```html
<!DOCTYPE html>
<html lang="en">
<head>
<meta charset="utf-8">
<title>Voltrane — Poster</title>
<link rel="stylesheet" href="https://fonts.googleapis.com/css2?family=Josefin+Sans:wght@200&family=League+Spartan:wght@600&display=swap">
<style>
  :root {
    --paper: #ffffff;
    --poster-blue: #20467a;
    --ink-light: #ffffff;
  }
  html, body {
    margin: 0;
    padding: 0;
    width: 888px;
    height: 1200px;
    overflow: hidden;
    background: var(--paper);
  }
  .poster {
    display: block;
    width: 888px;
    height: 1200px;
  }
  .poster__field { fill: var(--poster-blue); }
  .poster__pixel { fill: var(--ink-light); }
  .poster__tagline {
    fill: var(--ink-light);
    font-family: "League Spartan", "Helvetica Neue", Arial, sans-serif;
    font-weight: 600;
    font-size: 16px;
    text-transform: uppercase;
  }
  .poster__title {
    fill: var(--ink-light);
    font-family: "Josefin Sans", "Helvetica Neue", Arial, sans-serif;
    font-weight: 200;
    font-size: 112px;
  }
  .grad-edge { stop-color: var(--poster-blue); }
  .grad-core { stop-color: var(--ink-light); }
</style>
</head>
<body>
<svg class="poster" viewBox="0 0 888 1200" xmlns="http://www.w3.org/2000/svg">
  <defs>
    <linearGradient id="dissolve-fade" x1="0" y1="0" x2="1" y2="0">
      <stop offset="0" class="grad-edge"/>
      <stop offset="0.45" class="grad-core"/>
      <stop offset="1" class="grad-core"/>
    </linearGradient>
  </defs>

  <rect class="poster__field" x="54" y="48" width="780" height="1104"/>

  <text class="poster__tagline" x="444" y="141" text-anchor="middle" textLength="532" lengthAdjust="spacing">When some become immortal the rest of us are dead.</text>

  <g class="poster__drift">
    <rect class="poster__pixel" x="105" y="149" width="42" height="42"/>
    <rect class="poster__pixel" x="228" y="266" width="10" height="10"/>
    <rect class="poster__pixel" x="318" y="577" width="44" height="44"/>
  </g>

  <rect class="poster__emblem" role="img" aria-label="Title emblem: a white cloud dissolving into scattered square pixels on its left side" x="410" y="778" width="365" height="154" rx="70" fill="url(#dissolve-fade)"/>

  <text class="poster__title" x="135" y="1046" textLength="617" lengthAdjust="spacing">VOLTRANE</text>
</svg>
</body>
</html>
```